Powerpoint template for basic scientists studying immunology

We are an QFB-funded consortium of basic science researchers at academic centers in Boston, Philadelphia and Oxford, UK. We study why the immune system fails to get rid of Hepatitis C virus, and whether new antiviral treatments that reduce viral load improve immune function. We are looking for a powerpoint template that we can use as a "brand" for our research consortium. It would feature a logo (file attached) and should represent the fonts/colors contained in the logo. We we would present at meetings and to program officers at the QFB, but, if we ever get around to it, would also be on a website.

The scientific description is as follows:
Hepatitis C virus (HCV) infects 185 million persons worldwide, is the leading indication for liver transplantation and, in the US, has a higher mortaliy rate than HIV. The annual healthcare costs associated with HCV exceed $9 billion, a number expected to increase as the epidemic matures and end stage liver disease peaks over the next decade. By virtue of its remarkable predilection for persistence, HCV is a model chronic viral infection. Mounting evidence supports the idea that HCV, while inducing type I IFN expression, maintains chronicity by virtue of global suppression of host innate and adaptive immunity. The mainstay of treatment for the last two decades, IFN-α-based regimens are ineffective in many patient subgroups and have significant side effects. The recent development of highly effective direct acting antivirals (DAA) against HCV promises to alter the landscape of this devastating infection by offering curative therapy without IFN. However, it remains essential that we understand what type of immunity remains following pharmacological eradication of the virus because: a) many HCV infected subjects remain at risk for re-infection; and b) DAAs are only partially effective in some patient subgroups, particularly those with past treatment with IFN. The imminent availability of IFN-free treatment for HCV offers an unprecedented opportunity to understand broad questions about alterations in immunity in humans with cure of chronic infections. Until now, mechanistic dissection of human immune responses has been challenging due to limited ability to directly perturb the system. The organizing principle of this U19 Program therefore, is to capitalize on the unique opportunity to, for the first time, cure chronic viral infection in humans without immune modulation and interrogate the immunological changes that ensue. Thus, we have formulated the following central hypothesis for this Program: DAA-mediated cure of chronic HCV infection will lead to partial "resetting" of some immune abnormalities, but specific immunological defects will persist in some subjects that prevent development of optimal immunity to HCV. We will test this hypothesis through a set of integrated Projects and Cores.

Target Market(s)

scientists.

Industry/Entity Type

Biotechnology

Font styles to use
Sans Serif

Requirements
Must have
• Very clean, very simple. Mostly whitespace for puting graphs and data on. Colors, fonts should match the logo. Please see ppt example.
Should not have
• too much of the ppt covered with the logo.

```html
<!DOCTYPE html>
<html lang="en">
<head>
<meta charset="utf-8">
<title>Novacel Immune Consortium — Slide Template</title>
<link href="https://fonts.googleapis.com/css2?family=Lato:wght@400;700&family=Montserrat:wght@400;600;700&display=swap" rel="stylesheet">
<style>
:root{
  --green:#4aa70a;
  --green-light:#66b82a;
  --blue:#1a9ad9;
  --ink:#3a3a3a;
  --frame:#000;
  --slide-top:#ffffff;
  --slide-bottom:#e9e9e9;
  --strip:#e2e2e2;
  --chev:#a8a8a8;
  --row-dark:#4a4a4a;
  --row-dark2:#5c5c5c;
  --cat:#cfcfcf;
}
*{box-sizing:border-box;margin:0;padding:0}
html,body{width:1061px;height:1200px;overflow:hidden;background:var(--frame)}
.deck{
  width:1061px;height:1200px;padding:8px;
  display:grid;grid-template-columns:518px 518px;grid-template-rows:repeat(3,388px);
  gap:9px;
}
.slide{
  position:relative;overflow:hidden;
  background:linear-gradient(180deg,var(--slide-top) 0%,var(--slide-bottom) 100%);
  border-top:6px solid var(--green);
  font-family:"Lato",sans-serif;color:var(--ink);
}
.heading{
  position:absolute;left:22px;top:18px;
  font-family:"Montserrat",sans-serif;font-weight:700;font-size:27px;color:var(--ink);letter-spacing:-.2px;
}
.heading .accent{color:var(--green)}

/* footer strip */
.footer-strip{position:absolute;left:0;right:0;bottom:0;height:30px;background:var(--strip)}
.footer-tab{
  position:absolute;left:50%;bottom:0;transform:translateX(-50%);
  width:127px;height:36px;background:var(--green);border-radius:6px 6px 0 0;
  display:flex;align-items:center;justify-content:center;color:#fff;
  font-family:"Lato",sans-serif;font-weight:400;font-size:13px;white-space:nowrap;
}
.footer-chev{position:absolute;bottom:8px;width:10px;height:14px}
.footer-chev.prev{left:calc(50% - 86px)}
.footer-chev.next{left:calc(50% + 76px)}

/* brand lockup */
.brand{position:absolute;left:0;right:0;display:flex;align-items:center;justify-content:center;gap:9px}
.brand .dot{width:22px;height:22px;border-radius:50%;background:var(--green)}
.brand .brand-name{font-family:"Lato",sans-serif;font-weight:400;font-size:16px;color:#555;white-space:nowrap}

/* title / thank-you band */
.band{position:absolute;left:0;right:0;bottom:0;height:108px;background:var(--green);color:#fff;text-align:center}
.band .by{position:absolute;left:0;right:0;top:36px;font-size:14px}
.band .presenter{position:absolute;left:0;right:0;top:54px;font-size:15px;font-weight:700}
.band .arrow{position:absolute;top:13px;width:44px;height:82px}
.band .arrow.left{left:16px}
.band .arrow.right{right:16px}

/* title slide */
.title-main{position:absolute;left:0;right:0;top:50px;text-align:center;font-family:"Montserrat",sans-serif;font-weight:700;font-size:46px;letter-spacing:.5px;color:var(--ink)}
.title-main .accent{color:var(--blue)}
.title-sub{position:absolute;left:0;right:0;top:106px;text-align:center;font-family:"Montserrat",sans-serif;font-weight:400;font-size:37px;color:var(--ink)}
.title-sub .accent{color:var(--blue)}

/* about */
.about-body{position:absolute;left:22px;right:22px;top:66px;font-size:14px;line-height:1.38;text-align:justify}
.about-body p{margin-bottom:12px}
.about-body strong{color:var(--green);font-weight:700}

/* services */
.services-list{position:absolute;left:40px;top:68px;list-style:none}
.services-list li{font-size:18px;height:25px;line-height:25px;position:relative;padding-left:20px}
.services-list li::before{content:"";position:absolute;left:0;top:9px;width:7px;height:7px;background:var(--green);transform:rotate(45deg)}
.team-photo{position:absolute;left:230px;top:80px;width:250px;height:222px;border-radius:6px;
  background:linear-gradient(180deg,#d9dadc 0%,#6d7078 30%,#3e4046 70%,#cfcfd1 100%)}

/* table */
.data-table{position:absolute;left:24px;top:69px;width:470px;border-collapse:collapse;font-family:"Lato",sans-serif}
.data-table th{height:25px;font-family:"Montserrat",sans-serif;font-weight:700;font-size:13px;text-align:center}
.data-table th.col-cat{background:#a9a9a9;color:#333;width:233px}
.data-table th.col-opt1{background:var(--green);color:#fff;width:118px}
.data-table th.col-opt2{background:#3f3f3f;color:#fff;width:119px}
.data-table td{height:18px;font-size:10px;text-align:center}
.data-table tr.cat td{background:var(--cat);text-align:left;padding-left:12px;font-weight:700;font-size:10.5px;color:#333}
.data-table td.label{text-align:left;padding-left:29px;background:#fff;color:#444}
.data-table tr.alt td.label{background:#efefef}
.data-table td.opt1{background:var(--green);color:#fff}
.data-table tr.alt td.opt1{background:var(--green-light)}
.data-table td.opt2{background:var(--row-dark);color:#ddd}
.data-table tr.alt td.opt2{background:var(--row-dark2)}

/* contact */
.map{position:absolute;left:31px;top:72px;width:222px;height:219px;border:5px solid #fff;box-shadow:0 0 3px rgba(0,0,0,.35);
  background:linear-gradient(160deg,#e9e4cf 0%,#dcd7bf 45%,#b9d2e6 70%,#9dc2e0 100%)}
.contact-info{position:absolute;left:266px;top:74px;width:232px;font-size:9.5px;line-height:1.32;color:#444}
.contact-info .intro{text-align:justify;margin-bottom:8px}
.contact-info .intro strong{color:var(--green)}
.contact-info h4{color:var(--green);font-size:11px;font-weight:700;margin-top:5px}
.social{position:absolute;left:34px;top:314px;display:flex;align-items:center;gap:8px}
.social .sq{width:18px;height:18px;background:var(--green);border-radius:2px}
.social .handle{font-size:11px;font-weight:700;color:#444;margin-left:2px}
.social .handle span{color:var(--green)}

/* thank you */
.thanks{position:absolute;left:0;right:0;top:70px;text-align:center;font-family:"Montserrat",sans-serif;font-weight:700;font-size:66px;letter-spacing:-1px;color:var(--ink)}
.thanks .accent{color:var(--blue)}
</style>
</head>
<body>
<main class="deck">

  <section class="slide slide-title">
    <h1 class="title-main"><span class="accent">TITLE</span> PROJECT</h1>
    <p class="title-sub">subtext <span class="accent">presentation</span></p>
    <div class="brand" style="top:192px">
      <span class="dot"></span>
      <span class="brand-name">Novacel Immune Consortium</span>
    </div>
    <div class="band">
      <svg class="arrow left" viewBox="0 0 44 82"><polygon points="36,0 44,8 14,41 44,74 36,82 0,41" fill="#fff"/></svg>
      <div class="by">Presentation by</div>
      <div class="presenter">Alex Morgan</div>
      <svg class="arrow right" viewBox="0 0 44 82"><polygon points="8,0 0,8 30,41 0,74 8,82 44,41" fill="#fff"/></svg>
    </div>
  </section>

  <section class="slide slide-about">
    <h2 class="heading"><span class="accent">About</span> Company</h2>
    <div class="about-body">
      <p><strong>Lorem ipsum</strong> dolor sit amet, consectetuer adipiscing elit. Maecenas porttitor congue massa. Fusce posuere, magna sed pulvinar ultricies, purus lectus malesuada libero, sit amet commodo magna eros quis urna.</p>
      <p><strong>Nunc viverra imperdiet enim</strong>. Fusce est. Vivamus a tellus. Pellentesque habitant morbi tristique senectus et netus et malesuada fames ac turpis egestas. Proin pharetra nonummy pede. Mauris et orci.</p>
      <p><strong>Aenean nec lorem.</strong> In porttitor. Donec laoreet nonummy augue.</p>
      <p>Suspendisse dui purus, scelerisque at, vulputate vitae, pretium mattis, nunc. Mauris eget neque at sem venenatis eleifend. Ut nonummy.</p>
      <p><strong>Fusce aliquet pede non pede.</strong><br>Suspendisse dapibus lorem pellentesque magna. Integer nulla.</p>
    </div>
    <div class="footer-strip"></div>
    <svg class="footer-chev prev" viewBox="0 0 10 14"><polyline points="8,1 2,7 8,13" fill="none" stroke="var(--chev)" stroke-width="3"/></svg>
    <div class="footer-tab">Novacel Immune</div>
    <svg class="footer-chev next" viewBox="0 0 10 14"><polyline points="2,1 8,7 2,13" fill="none" stroke="var(--chev)" stroke-width="3"/></svg>
  </section>

  <section class="slide slide-services">
    <h2 class="heading"><span class="accent">Our</span> Services</h2>
    <ul class="services-list">
      <li>Lorem ipsum</li><li>Lorem ipsum</li><li>Lorem ipsum</li><li>Lorem ipsum</li><li>Lorem ipsum</li>
      <li>Lorem ipsum</li><li>Lorem ipsum</li><li>Lorem ipsum</li><li>Lorem ipsum</li><li>Lorem ipsum</li>
    </ul>
    <div class="team-photo" role="img" aria-label="Photo of a team of business people standing in a group"></div>
    <div class="footer-strip"></div>
    <svg class="footer-chev prev" viewBox="0 0 10 14"><polyline points="8,1 2,7 8,13" fill="none" stroke="var(--chev)" stroke-width="3"/></svg>
    <div class="footer-tab">Novacel Immune</div>
    <svg class="footer-chev next" viewBox="0 0 10 14"><polyline points="2,1 8,7 2,13" fill="none" stroke="var(--chev)" stroke-width="3"/></svg>
  </section>

  <section class="slide slide-table">
    <h2 class="heading"><span class="accent">Table</span> Presentation</h2>
    <table class="data-table">
      <thead><tr><th class="col-cat">CATEGORY</th><th class="col-opt1">OPTION 1</th><th class="col-opt2">OPTION 2</th></tr></thead>
      <tbody>
        <tr class="cat"><td colspan="3">Category 1</td></tr>
        <tr><td class="label">Lorem ipsum dolor sit amet</td><td class="opt1">Yes</td><td class="opt2">-</td></tr>
        <tr class="alt"><td class="label">Lorem ipsum dolor sit amet</td><td class="opt1">Yes</td><td class="opt2">-</td></tr>
        <tr><td class="label">Lorem ipsum dolor sit amet</td><td class="opt1">Yes</td><td class="opt2">-</td></tr>
        <tr class="cat"><td colspan="3">Category 2</td></tr>
        <tr><td class="label">Lorem ipsum dolor sit amet</td><td class="opt1">Yes</td><td class="opt2">-</td></tr>
        <tr class="alt"><td class="label">Lorem ipsum dolor sit amet</td><td class="opt1">Yes</td><td class="opt2">-</td></tr>
        <tr><td class="label">Lorem ipsum dolor sit amet</td><td class="opt1">Yes</td><td class="opt2">-</td></tr>
        <tr class="alt"><td class="label">Lorem ipsum dolor sit amet</td><td class="opt1">Yes</td><td class="opt2">-</td></tr>
        <tr class="cat"><td colspan="3">Category 3</td></tr>
        <tr><td class="label">Lorem ipsum dolor sit amet</td><td class="opt1">Yes</td><td class="opt2">-</td></tr>
        <tr class="alt"><td class="label">Lorem ipsum dolor sit amet</td><td class="opt1">Yes</td><td class="opt2">-</td></tr>
      </tbody>
    </table>
    <div class="footer-strip"></div>
    <svg class="footer-chev prev" viewBox="0 0 10 14"><polyline points="8,1 2,7 8,13" fill="none" stroke="var(--chev)" stroke-width="3"/></svg>
    <div class="footer-tab">Novacel Immune</div>
    <svg class="footer-chev next" viewBox="0 0 10 14"><polyline points="2,1 8,7 2,13" fill="none" stroke="var(--chev)" stroke-width="3"/></svg>
  </section>

  <section class="slide slide-contact">
    <h2 class="heading"><span class="accent">Contact</span> Info</h2>
    <div class="map" role="img" aria-label="Map of Europe and the Mediterranean region"></div>
    <div class="contact-info">
      <p class="intro"><strong>Lorem ipsum</strong> dolor sit amet, consectetuer adipiscing elit. Maecenas porttitor congue massa. Fusce posuere, magna sed pulvinar ultricies, purus lectus malesuada libero, sit amet commodo magna eros quis urna.</p>
      <h4>Address</h4>
      <p>88 Harbor Lane<br>Westfield, America<br>20451 (U.S.A)</p>
      <h4>Phone</h4>
      <p>0199-555-214</p>
      <h4>FAX</h4>
      <p>0199-555-214</p>
      <h4>Email</h4>
      <p>hello@novacelimmune.org</p>
      <h4>Website</h4>
      <p>www.novacelimmune.org</p>
    </div>
    <div class="social">
      <span class="sq"></span><span class="sq"></span><span class="sq"></span><span class="sq"></span>
      <span class="handle">@NOVACEL<span>IMMUNE</span></span>
    </div>
    <div class="footer-strip"></div>
    <svg class="footer-chev prev" viewBox="0 0 10 14"><polyline points="8,1 2,7 8,13" fill="none" stroke="var(--chev)" stroke-width="3"/></svg>
    <div class="footer-tab">Novacel Immune</div>
    <svg class="footer-chev next" viewBox="0 0 10 14"><polyline points="2,1 8,7 2,13" fill="none" stroke="var(--chev)" stroke-width="3"/></svg>
  </section>

  <section class="slide slide-thanks">
    <h2 class="thanks">Thank<span class="accent">You</span></h2>
    <div class="brand" style="top:196px">
      <span class="dot"></span>
      <span class="brand-name">Novacel Immune Consortium</span>
    </div>
    <div class="band">
      <svg class="arrow left" viewBox="0 0 44 82"><polygon points="36,0 44,8 14,41 44,74 36,82 0,41" fill="#fff"/></svg>
      <div class="by">Presentation by</div>
      <div class="presenter">Alex Morgan</div>
      <svg class="arrow right" viewBox="0 0 44 82"><polygon points="8,0 0,8 30,41 0,74 8,82 44,41" fill="#fff"/></svg>
    </div>
  </section>

</main>
</body>
</html>
```